2020 Teamwear Price List

Price list of our popular teamwear items that we wholesale to clubs and schools.
looking to create a price list with images, images can be obtained from our website:
www.kelvarrogearhouse.com.au
price list does not have to have lots of details about each product, just a from price. with minimum order etc.
and we can email or post to our clients, so it can be A4 pages/booklet style.
i can also provide images after i choose the design layout we like, so you can just use generic images for now if required.

Target Market(s)

Clubs and Schools

Font styles to use
Sans Serif

Colors

Designer to choose colors to be used in the design.

Requirements
Must have
• Photo or generated image for each product.
Nice to have
• simple format , easy to read , and easy to update from time to time

```html
<!DOCTYPE html>
<html lang="en">
<head>
<meta charset="utf-8">
<title>Kelvarro Gear House – Teamwear Price List</title>
<link rel="stylesheet" href="https://fonts.googleapis.com/css2?family=Josefin+Sans:wght@100;300;700&family=Open+Sans:wght@400;700;800&family=Oswald:wght@500&display=swap">
<style>
  :root {
    --stage: #d8d8d8;
    --ink: #2a2a2a;
    --ink-soft: #3a3a3a;
    --red: #d24c2f;
    --red-deep: #a9321f;
    --red-light: #dc6a52;
    --paper: #dcdcdc;
    --white: #ffffff;
    --blush: #f6c8bb;
    --muted: #c9c9c9;
  }
  * { box-sizing: border-box; margin: 0; padding: 0; }
  html, body { width: 1200px; height: 800px; overflow: hidden; }
  body {
    background: var(--stage);
    font-family: "Open Sans", Arial, sans-serif;
    position: relative;
  }
  .page {
    position: absolute;
    top: 50px;
    width: 495px;
    height: 700px;
    overflow: hidden;
    box-shadow: 0 6px 18px rgba(0,0,0,.18);
  }
  .page svg.page-shapes { position: absolute; inset: 0; }

  /* Brand name */
  .brand {
    position: absolute;
    left: 0; right: 0;
    display: flex;
    justify-content: center;
    align-items: center;
    gap: 8px;
    color: var(--white);
    font-family: "Open Sans", Arial, sans-serif;
    font-weight: 800;
    letter-spacing: .06em;
    text-transform: uppercase;
  }
  .brand-dot {
    width: 12px; height: 12px;
    border-radius: 50%;
    background: var(--red);
  }

  /* Cover */
  .cover { left: 80px; background: var(--paper); }
  .cover .brand { top: 58px; font-size: 19px; }
  .cover-title {
    position: absolute;
    top: 150px; left: 0; right: 0;
    text-align: center;
    color: var(--white);
    font-family: "Josefin Sans", Arial, sans-serif;
    line-height: .95;
  }
  .cover-title .main { display: block; font-weight: 700; font-size: 46px; letter-spacing: .04em; }
  .cover-title .sub { display: block; font-weight: 100; font-size: 42px; letter-spacing: .14em; }
  .cover-url {
    position: absolute;
    bottom: 36px; left: 0; right: 0;
    text-align: center;
    font-family: "Oswald", Arial, sans-serif;
    font-weight: 500;
    font-size: 12px;
    letter-spacing: .04em;
    color: var(--ink);
    text-transform: uppercase;
  }

  /* Inside price page */
  .price-page {
    left: 625px;
    background: linear-gradient(120deg, var(--red-deep) 0%, var(--red) 45%, var(--red-light) 100%);
  }
  .price-page .brand { top: 70px; font-size: 17px; }
  .price-note {
    position: absolute;
    top: 182px; left: 40px; right: 30px;
    color: var(--blush);
    font-size: 11.5px;
    line-height: 1.45;
    letter-spacing: .03em;
    text-align: right;
  }
  .product-row {
    position: absolute;
    left: 0; right: 0;
    height: 130px;
  }
  .product-band {
    position: absolute;
    left: 120px; right: 0;
    top: 30px;
    height: 58px;
    background: var(--ink-soft);
    display: flex;
    align-items: center;
    justify-content: flex-end;
    padding: 0 20px 0 58px;
    gap: 12px;
    color: var(--white);
  }
  .product-detail {
    font-size: 10px;
    color: var(--muted);
    letter-spacing: .04em;
    white-space: nowrap;
    align-self: flex-start;
    margin-top: 8px;
  }
  .product-name { text-align: left; line-height: 1.05; white-space: nowrap; }
  .product-name strong {
    display: block;
    font-weight: 800;
    font-size: 15px;
    letter-spacing: .1em;
    text-transform: uppercase;
  }
  .product-name span {
    display: block;
    font-family: "Josefin Sans", Arial, sans-serif;
    font-weight: 300;
    font-size: 20px;
    letter-spacing: .06em;
  }
  .product-name--long strong { font-size: 12px; letter-spacing: .05em; }
  .product-photo {
    position: absolute;
    left: 40px; top: 0;
    width: 125px; height: 118px;
    border: 5px solid var(--ink);
    background: linear-gradient(160deg, #e9e9e9 0%, #cfcfcf 100%);
  }
  .photo-polo { background: linear-gradient(160deg, #ececec 0%, #2f3550 60%, #d6d6d6 100%); }
  .photo-hoodie { background: linear-gradient(160deg, #e6e6e6 0%, #6d7f9c 60%, #d4d4d4 100%); }
  .photo-tee { background: linear-gradient(160deg, #eeeeee 0%, #c9302c 60%, #d8d8d8 100%); }
</style>
</head>
<body>

<section class="page cover" aria-label="Front cover">
  <svg class="page-shapes" viewBox="0 0 495 700" width="495" height="700" aria-hidden="true">
    <rect width="495" height="700" fill="var(--paper)"/>
    <path d="M0 0 H495 V372 Q250 362 0 340 Z" fill="var(--ink)"/>
    <path d="M0 340 Q250 362 495 372 V380 Q250 370 0 349 Z" fill="#e8e8e8"/>
    <path d="M0 349 Q250 370 495 380 V630 Q330 400 0 372 Z" fill="var(--red)"/>
  </svg>
  <div class="brand"><i class="brand-dot"></i>Kelvarro Gear House</div>
  <h1 class="cover-title">
    <span class="main">TEAMWEAR</span>
    <span class="sub">PRICE LIST</span>
  </h1>
  <p class="cover-url">www.kelvarrogearhouse.com.au</p>
</section>

<section class="page price-page" aria-label="Teamwear prices">
  <svg class="page-shapes" viewBox="0 0 495 700" width="495" height="700" aria-hidden="true">
    <path d="M0 0 H495 V120 Q360 190 230 170 Q90 150 0 60 Z" fill="var(--ink)"/>
  </svg>
  <div class="brand"><i class="brand-dot"></i>Kelvarro Gear House</div>
  <p class="price-note">Prices shown below exclude GST, Custom Clothing is based on order of 20 + units, smaller order quantities are available on request</p>

  <div class="product-row" style="top:260px">
    <div class="product-band">
      <span class="product-detail">with 1 logo embroidered</span>
      <div class="product-name"><strong>Club Polos</strong><span>$21.00</span></div>
    </div>
    <div class="product-photo photo-polo" role="img" aria-label="Photo of a model wearing a navy club polo"></div>
  </div>

  <div class="product-row" style="top:395px">
    <div class="product-band">
      <span class="product-detail">with 1 logo embroidered</span>
      <div class="product-name"><strong>Club Hoodie</strong><span>$29.00</span></div>
    </div>
    <div class="product-photo photo-hoodie" role="img" aria-label="Photo of a model wearing a grey-blue club hoodie"></div>
  </div>

  <div class="product-row" style="top:530px">
    <div class="product-band">
      <span class="product-detail">unlimited logos</span>
      <div class="product-name product-name--long"><strong>Sublimited Tee Shirts</strong><span>$35.00</span></div>
    </div>
    <div class="product-photo photo-tee" role="img" aria-label="Photo of a model wearing a red sublimated tee shirt"></div>
  </div>
</section>

</body>
</html>
```